The Marlow Wellness Studio (marlowstudio.example)

One page website (already purchased the theme) introducing the online clinic, with video, sections on the page our process, the technology, blog, the practitioner, contact, testimonials, find out more (see copy below) I am in the closing stages of having some collateral prepared I will load up the files that are in place so far so you get the feel for the brand and the current progress on the a brochure. The theme I have currently is loaded with demo data . this needs to be deleted and replaced. See here marlowstudio.example.

Target Market(s)

Female 30-50

Coding

Coded - Design and coding required

Number of Pages Required

1 page

Font styles to use
Serif
Sans Serif

Colors
33a6d7
3277b5

Requirements
Must have
• Consistent feel with existing A4 brochure, Trifold Brochure and business card,

Intro image & Outcome statement - Recharge Your Energy
Video & Free Access Offer
Why Energy
Our Process
About Vireq Technology
Getting Started
About Tobin
Our Services
Testimonials
Contact
Blog

Nice to have
• Suggestions for images.

```html
<!DOCTYPE html>
<html lang="en">
<head>
<meta charset="utf-8">
<title>The Marlow Wellness Studio</title>
<link href="https://fonts.googleapis.com/css2?family=Roboto:wght@400;500;700&family=Poppins:ital,wght@0,300;0,400;0,500;1,400&display=swap" rel="stylesheet">
<style>
:root{
  --teal:#64cbd5;
  --teal-mid:#57bfca;
  --teal-deep:#45adb9;
  --navy:#16172b;
  --ink:#1c1d24;
  --body:#6f7479;
  --muted:#9aa0a5;
  --mist:#eef8fa;
  --card:#f4f5f6;
  --line:#e3e8ea;
  --white:#ffffff;
}
*{margin:0;padding:0;box-sizing:border-box}
html,body{width:1200px;height:4898px;overflow:hidden;background:var(--white)}
body{font-family:"Poppins",sans-serif;color:var(--body);position:relative}
h1,h2,h3,h4{font-family:"Roboto",sans-serif;color:var(--ink)}
.section{position:absolute;left:0;width:1200px}
.abs{position:absolute}

/* header */
.site-header{top:0;height:76px;z-index:3}
.brand{left:42px;top:25px;display:flex;align-items:center;gap:8px;font-family:"Poppins",sans-serif;font-size:15px;font-weight:500;color:var(--teal)}
.brand-dot{width:22px;height:22px;border-radius:50%;background:var(--teal)}
.main-nav{left:434px;top:31px;display:flex;gap:18px;font-size:9.5px;text-transform:uppercase;color:var(--ink);letter-spacing:.2px}
.call-btn{left:998px;top:21px;width:158px;height:32px;border-radius:16px;background:var(--teal);color:var(--white);font-size:9.5px;display:flex;align-items:center;justify-content:center}

/* hero */
.hero{top:0;height:536px;background:var(--white);overflow:hidden}
.hero-photo{left:720px;top:0}
.hero h1{position:absolute;left:234px;top:196px;font-size:62px;line-height:64px;font-weight:700}
.hero-sub{left:234px;top:348px;font-size:12px;color:var(--body)}
.btn-pill{left:234px;top:390px;width:156px;height:34px;border-radius:17px;background:var(--teal);color:var(--white);font-size:11px;display:flex;align-items:center;justify-content:center}

/* why energy */
.why{top:536px;height:529px;background:var(--navy);overflow:hidden}
.why-visual{right:0;top:0;width:430px;height:529px;background:radial-gradient(ellipse at 55% 50%,#3a6f52 0%,#22402f 30%,#16172b 72%)}
.why h2{position:absolute;left:234px;top:60px;font-size:25px;color:var(--white);font-weight:700}
.why-list{left:234px;top:114px;width:540px;list-style:none}
.why-list li{position:relative;padding-left:20px;font-size:10.6px;line-height:17.5px;color:#e7e9ef;margin-bottom:15px}
.why-list li svg{position:absolute;left:0;top:4px}

/* process */
.process{top:1065px;height:732px;background:var(--mist)}
.process h2{position:absolute;left:0;width:1200px;text-align:center;top:58px;font-size:24px;font-weight:700}
.process-arch{left:48px;top:180px;width:392px;height:562px;border:3px solid #d8eef1;border-radius:196px 196px 0 0}
.process-photo{left:46px;top:190px;width:396px;height:490px;border-radius:198px 198px 0 0;background:linear-gradient(180deg,#eef8fa 0%,#dfe5ea 30%,#8a93a3 70%,#5b6578 100%)}
.process-card{left:485px;width:481px;height:126px;background:var(--white);border:1px solid var(--line)}
.process-card .icon{position:absolute;left:16px;top:18px}
.process-card h3{position:absolute;left:74px;top:19px;font-size:13px;font-weight:500}
.process-card p{position:absolute;left:74px;top:40px;width:392px;font-size:9px;line-height:16px;color:var(--muted)}
.process-card .num{position:absolute;right:14px;top:40px;font-family:"Roboto",sans-serif;font-size:46px;font-weight:700;color:#eef8fa}

/* steps */
.steps{top:1797px;height:709px;background:var(--white)}
.steps h2{position:absolute;left:234px;top:58px;font-size:24px;font-weight:700}
.step-card{width:231px;height:166px;background:var(--card);text-align:center}
.step-num{position:absolute;left:98px;top:22px;width:34px;height:34px;border-radius:50%;background:var(--white);font-family:"Roboto",sans-serif;font-size:11px;font-weight:700;color:var(--ink);display:flex;align-items:center;justify-content:center}
.step-card h3{position:absolute;left:0;width:231px;top:74px;font-size:13px;font-weight:500}
.step-card p{position:absolute;left:26px;width:179px;top:100px;font-size:9px;line-height:16px;color:var(--muted)}

/* practitioner */
.practitioner{top:2506px;height:689px;background:var(--mist)}
.portrait{left:234px;top:58px}
.practitioner h2{position:absolute;left:590px;top:48px;font-size:26px;font-weight:500}
.creds{left:590px;top:88px;font-size:9.5px;color:var(--ink)}
.accent-line{left:590px;top:112px;width:32px;height:2px;background:var(--teal)}
.bio-lead{left:590px;top:126px;width:400px;font-size:9.8px;line-height:17px}
.bio-strong{left:590px;top:172px;width:400px;font-size:9.8px;line-height:17px;color:var(--ink)}
.bio-list{left:590px;top:221px;list-style:none;font-size:8.6px;line-height:22.4px;color:var(--body)}
.bio-body{left:234px;width:730px;font-size:9.8px;line-height:17px}
.bio-quote{left:234px;top:460px;width:730px;font-size:13.5px;line-height:22px;font-style:italic;color:#4b5055}
.bio-quote b{font-style:normal;color:var(--ink)}

/* services */
.services{top:3195px;height:646px;background:var(--white)}
.services h2{position:absolute;left:234px;top:58px;font-size:24px;font-weight:700}
.svc-panel{left:253px;top:117px;width:287px;height:478px;background:var(--mist)}
.svc-col{top:117px;width:93px;height:478px;border:1px solid var(--line);background:var(--white)}
.svc-col h4{position:absolute;left:0;width:91px;text-align:center;top:20px;font-size:11px;font-weight:500}
.svc-row{left:266px;font-size:8.6px;color:var(--body)}
.svc-group{left:266px;font-size:11px;font-weight:500;color:var(--teal-mid)}
.svc-group small{font-size:8px;font-weight:400;color:var(--muted)}

/* technology */
.technology{top:3841px;height:381px;background:var(--mist)}
.technology h2{position:absolute;left:234px;top:62px;font-size:24px;font-weight:700}
.tech-text{width:352px;font-size:8.8px;line-height:17.6px}

/* testimonials */
.testimonials{top:4222px;height:437px;background:var(--white)}
.testimonials h2{position:absolute;left:0;width:1200px;text-align:center;top:58px;font-size:24px;font-weight:700}
.quote-card{top:120px;width:231px;height:266px;background:var(--white);border:1px solid var(--line);box-shadow:0 2px 8px rgba(0,0,0,.04);text-align:center}
.avatar{position:absolute;left:84px;top:18px;width:64px;height:64px;border-radius:50%;background:linear-gradient(160deg,#d9c3b4,#6b5a52)}
.quote-mark{position:absolute;left:0;width:229px;top:88px;font-family:"Roboto",sans-serif;font-size:18px;color:#c9d0d4;line-height:18px}
.quote-card h3{position:absolute;left:0;width:229px;top:110px;font-size:12.5px;font-weight:500}
.quote-card p{position:absolute;left:26px;width:179px;top:136px;font-size:8.8px;line-height:18px;color:var(--muted)}

/* contact */
.contact{top:4659px;height:182px}
.contact-panel{top:0;height:182px;color:var(--white);text-align:center}
.contact-panel .label{position:absolute;left:0;width:100%;top:56px;font-size:9px;text-transform:uppercase;letter-spacing:.3px}
.contact-panel .rule{position:absolute;left:50%;margin-left:-14px;top:76px;width:28px;height:1px;background:rgba(255,255,255,.8)}
.contact-panel .value{position:absolute;left:0;width:100%;top:94px;font-family:"Roboto",sans-serif;font-size:15.5px;font-weight:500;line-height:18px}
</style>
</head>
<body>

<header class="section site-header">
  <div class="abs brand"><span class="brand-dot"></span>The Marlow Wellness Studio</div>
  <nav class="abs main-nav">
    <span>Home</span><span>About Us</span><span>Services</span><span>Diseases</span><span>Testimonials</span><span>Price</span><span>Features</span><span>Contacts</span>
  </nav>
  <div class="abs call-btn">Call Us: (+999) 0100 2040</div>
</header>

<section class="section hero">
  <svg class="abs hero-photo" width="480" height="536" viewBox="0 0 480 536" role="img" aria-label="Photo of a joyful woman leaping in a golden meadow at sunset">
    <defs>
      <linearGradient id="sunset" x1="0" y1="0" x2="1" y2="1">
        <stop offset="0" stop-color="#f3c76a"/>
        <stop offset=".45" stop-color="#e39a3c"/>
        <stop offset="1" stop-color="#9a5a22"/>
      </linearGradient>
    </defs>
    <path d="M70 0 C40 80 190 120 190 220 C190 330 300 430 480 520 L480 0 Z" fill="url(#sunset)"/>
    <path d="M70 0 C40 80 190 120 190 220 C190 330 300 430 480 520" fill="none" stroke="#64cbd5" stroke-width="6"/>
  </svg>
  <h1>Restore<br>your Energy</h1>
  <p class="abs hero-sub">for exceptional health and longevity</p>
  <div class="abs btn-pill">Learn More</div>
</section>

<section class="section why">
  <div class="abs why-visual" role="img" aria-label="Glowing network illustration of a human head in profile"></div>
  <h2>Why “Energy”?</h2>
  <ul class="abs why-list">
    <li><svg width="11" height="9" viewBox="0 0 11 9"><path d="M1 4.5l3 3 6-6" fill="none" stroke="#64cbd5" stroke-width="1.6"/></svg>It seems like an obvious answer, after all, “more energy please” is top of the wish list for most of our clients.</li>
    <li><svg width="11" height="9" viewBox="0 0 11 9"><path d="M1 4.5l3 3 6-6" fill="none" stroke="#64cbd5" stroke-width="1.6"/></svg>But you may not know how vital energy is to how you feel.</li>
    <li><svg width="11" height="9" viewBox="0 0 11 9"><path d="M1 4.5l3 3 6-6" fill="none" stroke="#64cbd5" stroke-width="1.6"/></svg>At cellular level, mitochondria are responsible for the functioning every cell in every organ and every system of your body, every second of your existence. If mitochondrial operation is under stress, you will feel it.</li>
    <li><svg width="11" height="9" viewBox="0 0 11 9"><path d="M1 4.5l3 3 6-6" fill="none" stroke="#64cbd5" stroke-width="1.6"/></svg>But true to the teachings of traditional Chinese Medicine, energy flows, it can get stuck, and of course certain types of energy can be a hinderance to optimal operations as well.</li>
    <li><svg width="11" height="9" viewBox="0 0 11 9"><path d="M1 4.5l3 3 6-6" fill="none" stroke="#64cbd5" stroke-width="1.6"/></svg>At the marlowstudio.example we don’t like you to guess.</li>
    <li><svg width="11" height="9" viewBox="0 0 11 9"><path d="M1 4.5l3 3 6-6" fill="none" stroke="#64cbd5" stroke-width="1.6"/></svg>We encourage you to test!</li>
    <li><svg width="11" height="9" viewBox="0 0 11 9"><path d="M1 4.5l3 3 6-6" fill="none" stroke="#64cbd5" stroke-width="1.6"/></svg>Using state of the art bioenergetic home based scanning technology, you can detect why you feel the way you feel, and direct your attention to the areas most in need.</li>
    <li><svg width="11" height="9" viewBox="0 0 11 9"><path d="M1 4.5l3 3 6-6" fill="none" stroke="#64cbd5" stroke-width="1.6"/></svg>You can buy prescription free energy drops to correct for blocks or energetic disrepair, or you can seek a consultation to get a prescription to assist you.</li>
  </ul>
</section>

<section class="section process">
  <h2>Our Process</h2>
  <div class="abs process-arch"></div>
  <div class="abs process-photo" role="img" aria-label="Photo of a woman meditating cross-legged"></div>

  <article class="abs process-card" style="top:115px">
    <svg class="icon" width="40" height="40" viewBox="0 0 40 40" fill="none" stroke="#1c1d24" stroke-width="1.5"><path d="M4 12V4h8M28 4h8v8M36 28v8h-8M12 36H4v-8"/><circle cx="20" cy="16" r="5" stroke="#64cbd5"/><path d="M11 31c1-6 5-9 9-9s8 3 9 9"/></svg>
    <h3>Detect</h3>
    <p>Use our body-field scanner, at home to uncover why you feel the way you do. With a single click, and in seconds, it returns a richly detailed overview – including multiple screens and beautiful graphics depicting the state of the Body-Field and how it supports the body’s wellness.</p>
    <span class="num">1</span>
  </article>
  <article class="abs process-card" style="top:260px">
    <svg class="icon" width="40" height="40" viewBox="0 0 40 40" fill="none" stroke="#1c1d24" stroke-width="1.5"><circle cx="8" cy="8" r="3"/><circle cx="20" cy="8" r="3" stroke="#64cbd5"/><circle cx="32" cy="8" r="3"/><path d="M4 18c0-3 8-3 8 0M16 18c0-3 8-3 8 0M28 18c0-3 8-3 8 0M8 20l12 8 12-8M20 28v8"/></svg>
    <h3>Direct</h3>
    <p>Use our body-field scanner, at home to uncover why you feel the way you do. With a single click, and in seconds, it returns a richly detailed overview – including multiple screens and beautiful graphics depicting the state of the Body-Field and how it supports the body’s wellness.</p>
    <span class="num">2</span>
  </article>
  <article class="abs process-card" style="top:405px">
    <svg class="icon" width="40" height="40" viewBox="0 0 40 40" fill="none" stroke="#1c1d24" stroke-width="1.6"><path d="M20 4l14 5v10c0 9-6 15-14 18C12 34 6 28 6 19V9z"/><path d="M14 20l4 4 8-8" stroke="#64cbd5"/></svg>
    <h3>Correct</h3>
    <p>Use our body-field scanner, at home to uncover why you feel the way you do. With a single click, and in seconds, it returns a richly detailed overview – including multiple screens and beautiful graphics depicting the state of the Body-Field and how it supports the body’s wellness.</p>
    <span class="num">3</span>
  </article>
  <article class="abs process-card" style="top:550px">
    <svg class="icon" width="40" height="40" viewBox="0 0 40 40" fill="none" stroke-width="1.8"><path d="M17 23l-5 5a5 5 0 01-7-7l5-5a5 5 0 017 0" stroke="#1c1d24"/><path d="M23 17l5-5a5 5 0 017 7l-5 5a5 5 0 01-7 0" stroke="#64cbd5"/><path d="M16 24l8-8" stroke="#1c1d24"/></svg>
    <h3>Re-Connect</h3>
    <p>Use our body-field scanner, at home to uncover why you feel the way you do. With a single click, and in seconds, it returns a richly detailed overview – including multiple screens and beautiful graphics depicting the state of the Body-Field and how it supports the body’s wellness.</p>
    <span class="num">4</span>
  </article>
</section>

<section class="section steps">
  <h2>Steps to Getting Started</h2>
  <div class="abs step-card" style="left:234px;top:118px"><span class="step-num">1</span><h3>Register</h3><p>Get your lifetime access to our platform and access many benefits free: marlowstudio.example/vireq</p></div>
  <div class="abs step-card" style="left:484px;top:118px"><span class="step-num">2</span><h3>Scanner</h3><p>Buy a scanner in the shop within your account at portal.vireqhealth.example (or beg or borrow from friend of family member)</p></div>
  <div class="abs step-card" style="left:734px;top:118px"><span class="step-num">3</span><h3>Download</h3><p>Download the smart phone app Vitalis</p></div>
  <div class="abs step-card" style="left:234px;top:303px"><span class="step-num">4</span><h3>Scan</h3><p>Pair your scanner, with the app and follow instructions on how to scan</p></div>
  <div class="abs step-card" style="left:484px;top:303px"><span class="step-num">5</span><h3>View</h3><p>View your results on you phone or sign back online for better viewing experience</p></div>
  <div class="abs step-card" style="left:734px;top:303px"><span class="step-num">6</span><h3>Self Direct</h3><p>Follow simple guidelines on how to improve your results, or buy a “Feel Good” vitadrops or</p></div>
  <div class="abs step-card" style="left:234px;top:488px"><span class="step-num">7</span><h3>Get Help</h3><p>Contact us for help if you need more or you are eligible for a consultation, health strategy session or holistic coaching</p></div>
</section>

<section class="section practitioner">
  <svg class="abs portrait" width="286" height="318" viewBox="0 0 286 318" role="img" aria-label="Portrait photo of practitioner Tobin R Ashdown">
    <defs><linearGradient id="portraitTone" x1="0" y1="0" x2="0" y2="1"><stop offset="0" stop-color="#c8ccd0"/><stop offset=".55" stop-color="#9aa3ad"/><stop offset="1" stop-color="#5f7590"/></linearGradient></defs>
    <path d="M40 40 C90 -10 220 -5 265 50 C300 100 285 230 250 285 C215 330 90 325 40 285 C0 250 -5 95 40 40 Z" fill="url(#portraitTone)"/>
  </svg>
  <h2>Tobin R Ashdown</h2>
  <p class="abs creds">FDN-P HPC PFC PBC</p>
  <span class="abs accent-line"></span>
  <p class="abs bio-lead">Tobin is a multimodality alternative health provider with a focus in shedding light on what holds you back from being as healthy as you want.</p>
  <p class="abs bio-strong">He is a pioneer in the alternative health care space, and has established the Marlow Studio to help you to:</p>
  <ul class="abs bio-list">
    <li>- Understand why you feel the way you do</li>
    <li>- Do to the right things to change your energy</li>
    <li>- Be empowered to do it yourself, or be guided by a practitioner</li>
    <li>- Give you online flexibility where ever you are in the world</li>
    <li>- Bring the cutting edge diagnostic technology into your home</li>
    <li>- Enjoy lifetime access to the software, for FREE</li>
  </ul>
  <p class="abs bio-body" style="top:410px">It took Tobin almost 3 decades of trial and error, and false hope, for him to arrive at the same conclusion that leading experts in the field of bioenergetics had been saying since the beginning: energy drives biochemistry, not the other way round.</p>
  <p class="abs bio-quote">“in essence, Vireq gives you night goggles on what is going on for you, moreover what you can do about it. This is truly the future of medicine” <b>Tobin R Ashdown.</b></p>
  <p class="abs bio-body" style="top:522px">He has adopted the Vireq Health approach to supporting his programs that lead is clients to uncover what is holding them back from their health goals, and integrates complementary frameworks drawing on his diverse trainings and experience in.</p>
  <p class="abs bio-body" style="top:570px">Tobin is a certified Vireq Health Practitioner, Functional Diagnostic Nutrition Practitioner, Human Potential Coach, Psychological Fitness Coach, Primal Pathway Coach and a Heart Rhythm facilitator. Tobin is a former investment banker, venture capital adviser and an aerobatic pilot but now has his feet firmly on the ground on his mission to raise awareness of energy and how it can be used to drive exceptional health, longevity and performance outcomes.</p>
</section>

<section class="section services">
  <h2>Our Services</h2>
  <div class="abs svc-panel"></div>
  <div class="abs svc-col" style="left:555px"><h4>Free</h4></div>
  <div class="abs svc-col" style="left:661px"><h4>Active</h4></div>
  <div class="abs svc-col" style="left:767px"><h4>Strategy</h4></div>
  <div class="abs svc-col" style="left:873px"><h4>Transform</h4></div>

  <p class="abs svc-group" style="top:150px">Personal Account</p>
  <p class="abs svc-row" style="top:180px">Bioenergetic Music</p>
  <p class="abs svc-row" style="top:204px">Turning Tide – The Film</p>
  <p class="abs svc-row" style="top:228px">Bioenergetic Receipes</p>
  <p class="abs svc-row" style="top:252px">Bioenergetic Exercises</p>
  <p class="abs svc-row" style="top:276px">Vitalis Life Book</p>
  <p class="abs svc-group" style="top:311px">Bioenergetic Scans</p>
  <p class="abs svc-row" style="top:341px">Scanner</p>
  <p class="abs svc-row" style="top:366px">Unlimited Lifetime Body Scans</p>
  <p class="abs svc-group" style="top:401px">Consulting</p>
  <p class="abs svc-row" style="top:429px">Scan Interpretation Call</p>
  <p class="abs svc-row" style="top:455px">Group Webinar Scan Trainings</p>
  <p class="abs svc-row" style="top:481px">Full Intake &amp; Strategy &amp; 30 Day Program</p>
  <p class="abs svc-row" style="top:507px">1 * Coaching Call</p>
  <p class="abs svc-group" style="top:541px">Bespoke 90 Day Coaching <small>(By Application)</small></p>

  <svg class="abs" style="left:555px;top:0" width="420" height="600" viewBox="0 0 420 600" fill="none" stroke="#45adb9" stroke-width="1.6">
    <defs><path id="tk" d="M-5 0l3.5 3.5 6.5-6.5"/></defs>
    <use href="#tk" x="46" y="184"/><use href="#tk" x="46" y="208"/><use href="#tk" x="46" y="232"/><use href="#tk" x="46" y="256"/><use href="#tk" x="46" y="280"/>
    <use href="#tk" x="152" y="184"/><use href="#tk" x="152" y="208"/><use href="#tk" x="152" y="232"/><use href="#tk" x="152" y="256"/><use href="#tk" x="152" y="280"/>
    <use href="#tk" x="152" y="345"/><use href="#tk" x="152" y="370"/><use href="#tk" x="152" y="433"/><use href="#tk" x="152" y="459"/>
    <use href="#tk" x="258" y="184"/><use href="#tk" x="258" y="208"/><use href="#tk" x="258" y="232"/><use href="#tk" x="258" y="256"/><use href="#tk" x="258" y="280"/>
    <use href="#tk" x="258" y="345"/><use href="#tk" x="258" y="370"/><use href="#tk" x="258" y="433"/><use href="#tk" x="258" y="459"/><use href="#tk" x="258" y="485"/><use href="#tk" x="258" y="511"/><use href="#tk" x="258" y="546"/>
    <use href="#tk" x="364" y="184"/><use href="#tk" x="364" y="208"/><use href="#tk" x="364" y="232"/><use href="#tk" x="364" y="256"/><use href="#tk" x="364" y="280"/>
    <use href="#tk" x="364" y="345"/><use href="#tk" x="364" y="370"/><use href="#tk" x="364" y="433"/><use href="#tk" x="364" y="459"/><use href="#tk" x="364" y="485"/><use href="#tk" x="364" y="511"/><use href="#tk" x="364" y="546"/>
  </svg>
</section>

<section class="section technology">
  <h2>About Vireq Technology</h2>
  <p class="abs tech-text" style="left:234px;top:118px">Vireq Health is the leader in bioenergetics: the study, detection, and correction of energy in living systems. They spent decades mapping out the energy and communication systems of the body. Collectively, these are called the human body-field, which acts as a control system for the body’s physical activity.</p>
  <p class="abs tech-text" style="left:234px;top:222px">At the Marlow Studio, we furnish you with their scanning technology to provide you with a holistic wellness report in just seconds, from the comfort of your home. While this isn’t a medical assessment, the scan’s bioenergetic matching process often shows a strong correlation to known health concerns. But more important, this approach looks for the underlying problem so we can address health concerns from their roots with their bioenergetic solutions.</p>
  <p class="abs tech-text" style="left:608px;top:118px">The Vireq software directs you specifically to exercises, routines, affirmations, to improve your results. It will offer some guidance on the take energy drops to take, called Vitadrops. Without a practitioner, you may purchase on of the 19 Feel Good vitadrops. Otherwise you will need to will need to see a practitioner for strategy and prescription.</p>
  <p class="abs tech-text" style="left:608px;top:222px">When this field is underpowered or distorted, it’s unable to run the body in an optimal way and the body’s cells and systems may begin to fail. Symptoms often begin with simply feeling tired, but they can continue into just about any known health problem. When we improve function of the body-field, and we continue this with good nutrition and lifestyle choices, the body’s incredible healing system can take over and begin restoring the body to health.</p>
</section>

<section class="section testimonials">
  <h2>Testimonials</h2>
  <article class="abs quote-card" style="left:234px">
    <div class="avatar" role="img" aria-label="Profile photo of Dr Helen Marsh"></div>
    <span class="quote-mark">“</span>
    <h3>Dr Helen Marsh</h3>
    <p>“Vireq Health truly offers insights into the body, both mind and physical well-being, that the medical community cannot comprehend often, nor understand. It is truly a remarkable system”</p>
  </article>
  <article class="abs quote-card" style="left:484px">
    <div class="avatar" role="img" aria-label="Profile photo of Dr. Owen Pryce"></div>
    <span class="quote-mark">“</span>
    <h3>Dr. Owen Pryce, MD</h3>
    <p>“provides the signal for the body to heal itself. What’s hard to understand is it really doesn’t do anything except provide the signal. The body does everything else”</p>
  </article>
  <article class="abs quote-card" style="left:734px">
    <div class="avatar" role="img" aria-label="Profile photo of Clara Whitfield"></div>
    <span class="quote-mark">“</span>
    <h3>Clara Whitfield</h3>
    <p>“Thanks to Vireq, my energy has skyrocketed and I am accomplishing more than I have in years”</p>
  </article>
</section>

<section class="section contact">
  <div class="abs contact-panel" style="left:234px;width:244px;background:var(--teal)"><span class="label">Email Address</span><span class="rule"></span><span class="value">info@marlowstudio.example</span></div>
  <div class="abs contact-panel" style="left:478px;width:243px;background:var(--teal-mid)"><span class="label">Telephone</span><span class="rule"></span><span class="value">612 0100 0199</span></div>
  <div class="abs contact-panel" style="left:721px;width:245px;background:var(--teal-deep)"><span class="label">Address</span><span class="rule"></span><span class="value">Level 4, 27 Harbour Lane,<br>Sydney, Australia</span></div>
</section>

</body>
</html>
```